Re-Design WP Site BrightPebbles.info

Site Re-design. Also Need a Button for contact on main page. Need Great Looking products re designed. Also bonus if you can install a site SEO checker on the site.

BrightPebbles.info

```html
<!DOCTYPE html>
<html lang="en">
<head>
<meta charset="utf-8">
<title>BrightPebbles – We Are Digital Innovators</title>
<link href="https://fonts.googleapis.com/css2?family=Montserrat:wght@300;400;500;600;700&display=swap" rel="stylesheet">
<style>
:root{
  --bg-hero:#eceef2;
  --blue:#1a8fe3;
  --blue-bright:#0aa0f6;
  --navy:#2c4a9a;
  --heading:#3a5688;
  --ink:#222;
  --muted:#555;
  --line:#cfd3da;
  --footer:#262626;
  --white:#fff;
}
*{margin:0;padding:0;box-sizing:border-box}
html,body{width:1200px;height:2830px;overflow:hidden}
body{font-family:'Montserrat',sans-serif;color:var(--ink);background:var(--white);position:relative}
.abs{position:absolute}
.btn{position:absolute;display:flex;align-items:center;justify-content:center;color:var(--white);font-size:13px;background:linear-gradient(90deg,var(--blue-bright),var(--navy));text-transform:uppercase}
.hero-bg{position:absolute;left:0;top:0;width:1200px;height:720px;background:linear-gradient(180deg,var(--bg-hero) 0%,var(--bg-hero) 70%,#f6f7f9 100%)}
.wave{position:absolute;left:0;top:600px;width:1200px;height:140px}
.brand{left:145px;top:44px;font-size:26px;font-weight:600;color:var(--blue);letter-spacing:.3px}
.brand-tag{left:185px;top:75px;font-size:10px;color:var(--ink)}
.nav{left:603px;top:59px;display:flex;gap:17px;font-size:13px;color:#333}
.nav .active{color:var(--blue)}
.hero-kicker{left:142px;top:172px;font-size:40px;font-weight:300;color:var(--heading)}
.hero-title{left:138px;top:215px;font-size:52px;font-weight:700;color:var(--heading);line-height:58px}
.hero-copy{left:142px;top:328px;width:430px;font-size:12.7px;line-height:23px;color:#222;white-space:nowrap}
.dots{left:63px;top:289px}
.dots span{display:block;width:12px;height:12px;border-radius:50%;background:#c9cbcf;margin-bottom:9px}
.dots span.on{width:17px;height:17px;margin-left:-2px;background:linear-gradient(135deg,var(--blue-bright),var(--navy))}
.input{position:absolute;background:var(--white);border:1px solid #e1e3e7;box-shadow:0 3px 6px rgba(0,0,0,.12);font-size:14px;color:#555;padding-left:21px;display:flex;align-items:center}
.art{position:absolute}
.section-title{position:absolute;left:0;width:1200px;text-align:center;font-weight:400}
.rule{position:absolute;height:3px;background:var(--blue)}
.lead{position:absolute;left:0;width:1200px;text-align:center;font-size:14px;line-height:24px;color:#222}
.feature-icon{position:absolute;width:70px;height:70px;border-radius:50%;border:2px solid var(--navy)}
.feature-title{position:absolute;left:770px;font-size:17px;font-weight:500;color:#222}
.feature-copy{position:absolute;left:771px;font-size:13.5px;line-height:20px;color:#222}
.split-light{left:143px;top:1420px;font-size:32px;font-weight:300;color:#222}
.split-bold{left:142px;top:1455px;font-size:30px;font-weight:600;color:var(--navy)}
.split-copy{left:142px;top:1539px;width:410px;font-size:14px;line-height:24px;color:#444}
.checks{left:142px;top:1668px;display:flex;font-size:15px;color:var(--navy)}
.checks span{display:flex;align-items:center;gap:7px}
.info{position:absolute;display:flex;align-items:center;gap:16px;font-size:13.5px;line-height:19px;color:#444}
.info .ico{width:48px;height:48px;border-radius:50%;background:linear-gradient(135deg,var(--blue-bright),var(--navy));display:flex;align-items:center;justify-content:center;flex:none}
.label{position:absolute;font-size:13.5px;color:#333}
.field{position:absolute;width:371px;border:1px solid var(--line);background:var(--white)}
.footer{position:absolute;left:0;top:2650px;width:1200px;height:180px;background:var(--footer);color:var(--white)}
.social{position:absolute;top:45px;left:0;width:1200px;display:flex;justify-content:center;gap:36px}
.social span{width:20px;height:20px;border-radius:50%;border:3px solid var(--blue)}
.foot-nav{position:absolute;top:94px;left:0;width:1200px;display:flex;justify-content:center;gap:16px;font-size:14px}
.credit{position:absolute;top:130px;left:0;width:1200px;text-align:center;font-size:14px}
</style>
</head>
<body>

<div class="hero-bg"></div>
<svg class="wave" viewBox="0 0 1200 140" preserveAspectRatio="none" aria-hidden="true">
  <path d="M0 80 C250 10 450 30 650 80 C850 130 1050 120 1200 60 L1200 140 L0 140 Z" fill="#ffffff"/>
</svg>

<header>
  <div class="abs brand">BRIGHT PEBBLES</div>
  <div class="abs brand-tag">WE ARE DIGITAL INNOVATORS</div>
  <nav class="abs nav">
    <span class="active">HOME</span><span>SHOP</span><span>SOLUTIONS</span><span>BLOG</span><span>CONTACT</span>
  </nav>
  <div class="btn" style="left:963px;top:53px;width:92px;height:29px">Sign in</div>
</header>

<section class="hero">
  <div class="abs dots"><span></span><span></span><span></span><span class="on"></span></div>
  <div class="abs hero-kicker">We Are</div>
  <h1 class="abs hero-title">Digital<br>Innovators</h1>
  <p class="abs hero-copy">We’re a studio of creators inventing unique and effective<br>IT applications providing solutions that solve real world problems.</p>
  <div class="input" style="left:144px;top:394px;width:340px;height:43px">Email address</div>
  <div class="btn" style="left:147px;top:451px;width:92px;height:29px">Sign in</div>
  <svg class="abs" style="left:444px;top:480px" width="114" height="30" viewBox="0 0 114 30" aria-hidden="true">
    <path d="M2 10 C35 25 75 28 110 6" stroke="#111" stroke-width="2.5" fill="none"/>
    <path d="M96 4 L111 5 L103 16" stroke="#111" stroke-width="2.5" fill="none"/>
  </svg>
  <div class="art" role="img" aria-label="Illustration of a team analysing charts on a large monitor with a magnifying glass" style="left:591px;top:156px;width:522px;height:432px;background:linear-gradient(135deg,#ffffff 0%,#e9f3fb 45%,#cfe6f5 100%);box-shadow:0 0 18px rgba(90,170,220,.35)"></div>
</section>

<section class="features">
  <h2 class="section-title" style="top:728px;font-size:40px">Our Feature &amp; Solutions</h2>
  <div class="rule" style="left:568px;top:792px;width:64px"></div>
  <p class="lead" style="top:815px">Sed ut perspiciatis unde omnis iste natus error sit voluptatem accusantium doloremque<br>laudantium, totam rem aperiam, eaque ipsa quae ab illo inventore veritatis et quasi architecto<br>beatae vitae dicta sunt explicabo.</p>
  <div class="art" role="img" aria-label="Isometric illustration of people working with a computer and a data dashboard" style="left:150px;top:910px;width:445px;height:355px;background:linear-gradient(160deg,#ffffff 0%,#e6e8fb 40%,#3a3aa0 75%,#ffffff 100%)"></div>

  <div class="feature-icon" style="left:682px;top:941px"></div>
  <div class="feature-title" style="top:940px">Nemo enim ipsam</div>
  <div class="feature-copy" style="top:968px">Nemo enim ipsam voluptatem quia voluptas<br>sit aspernatur aut odit aut fugit, sed quia</div>

  <div class="feature-icon" style="left:682px;top:1037px"></div>
  <div class="feature-title" style="top:1036px">Enim ipsam voluptatem</div>
  <div class="feature-copy" style="top:1064px">Nemo enim ipsam voluptatem quia voluptas<br>sit aspernatur aut odit aut fugit, sed quia</div>

  <div class="feature-icon" style="left:682px;top:1133px"></div>
  <div class="feature-title" style="top:1132px">ipsam voluptatem</div>
  <div class="feature-copy" style="top:1160px">Nemo enim ipsam voluptatem quia voluptas<br>sit aspernatur aut odit aut fugit, sed quia</div>

  <div class="btn" style="left:496px;top:1246px;width:209px;height:29px">Explore our offerings</div>
</section>

<section class="split">
  <div class="abs split-light">Nemo enim ipsam</div>
  <div class="abs split-bold">voluptatem quia voluptas</div>
  <div class="rule" style="left:142px;top:1513px;width:64px"></div>
  <p class="abs split-copy">Sed ut perspiciatis unde omnis iste natus error sit voluptatem accusantium doloremque laudantium, totam rem aperiam, eaque ipsa quae ab illo inventore veritatis et quasi architecto beatae vitae dicta sunt explicabo. Nemo enim ipsam voluptatem quia</p>
  <div class="abs checks">
    <span style="width:136px"><svg width="14" height="11" viewBox="0 0 14 11"><path d="M1 6 L5 10 L13 1" stroke="#1a8fe3" stroke-width="2.5" fill="none"/></svg>Looks great</span>
    <span style="width:135px"><svg width="14" height="11" viewBox="0 0 14 11"><path d="M1 6 L5 10 L13 1" stroke="#1a8fe3" stroke-width="2.5" fill="none"/></svg>Easy to use</span>
    <span><svg width="14" height="11" viewBox="0 0 14 11"><path d="M1 6 L5 10 L13 1" stroke="#1a8fe3" stroke-width="2.5" fill="none"/></svg>Try it yourself!</span>
  </div>
  <div class="btn" style="left:142px;top:1707px;width:210px;height:29px">Explore our offerings</div>
  <div class="art" role="img" aria-label="Isometric illustration of a laptop showing a profile with star ratings, a plant and a person" style="left:640px;top:1383px;width:433px;height:395px;background:linear-gradient(150deg,#ffffff 0%,#dfe6fb 45%,#9fb6ef 70%,#ffffff 100%)"></div>
</section>

<section class="contact">
  <h2 class="section-title" style="top:1893px;font-size:36px">Contact Us</h2>
  <div class="rule" style="left:568px;top:1949px;width:64px;height:2px"></div>
  <p class="section-title" style="top:1963px;font-size:20px">Have any questions? BrightPebbles to reach out.</p>

  <div class="info" style="left:250px;top:2044px">
    <span class="ico"><svg width="18" height="24" viewBox="0 0 18 24"><path d="M9 1 C4 1 1 5 1 9 C1 15 9 23 9 23 C9 23 17 15 17 9 C17 5 14 1 9 1 Z" fill="#fff"/><circle cx="9" cy="9" r="3.2" fill="#1a8fe3"/></svg></span>
    <span>BrightPebbles<br>26 Aliquam ac enim<br>placerat, sagittis purus et</span>
  </div>
  <div class="info" style="left:554px;top:2046px">
    <span class="ico"><svg width="22" height="22" viewBox="0 0 24 24"><path d="M6.6 10.8a15 15 0 0 0 6.6 6.6l2.2-2.2a1 1 0 0 1 1-.25 11.4 11.4 0 0 0 3.6.57 1 1 0 0 1 1 1V20a1 1 0 0 1-1 1A17 17 0 0 1 3 4a1 1 0 0 1 1-1h3.5a1 1 0 0 1 1 1c0 1.250.2 2.450.57 3.6a1 1 0 0 1-.25 1z" fill="#fff"/></svg></span>
    <span>Phone<br>0123 456 789</span>
  </div>
  <div class="info" style="left:778px;top:2046px">
    <span class="ico"><svg width="24" height="18" viewBox="0 0 24 18"><rect x="1" y="1" width="22" height="16" rx="2" fill="#fff"/><path d="M1 3 L12 10 L23 3" stroke="#1a8fe3" stroke-width="2" fill="none"/></svg></span>
    <span>Email<br>info@brightpebbles.info</span>
  </div>

  <form>
    <label class="label" style="left:215px;top:2139px">Name *</label>
    <div class="field" style="left:215px;top:2167px;height:63px"></div>
    <label class="label" style="left:615px;top:2139px">Company</label>
    <div class="field" style="left:615px;top:2167px;height:63px"></div>
    <label class="label" style="left:215px;top:2251px">Email *</label>
    <div class="field" style="left:215px;top:2279px;height:63px"></div>
    <label class="label" style="left:615px;top:2251px">Comment or Message *</label>
    <div class="field" style="left:615px;top:2279px;height:175px"></div>
    <label class="label" style="left:215px;top:2363px">Phone</label>
    <div class="field" style="left:215px;top:2391px;height:63px"></div>
    <div class="btn" style="left:476px;top:2484px;width:249px;height:50px;font-size:20px">Submit</div>
  </form>
</section>

<footer class="footer">
  <div class="social" aria-label="Social links"><span></span><span></span><span></span></div>
  <nav class="foot-nav"><span>HOME</span><span>SHOP</span><span>SOLUTIONS</span><span>BLOG</span><span>CONTACT</span></nav>
  <p class="credit">Developed by Northfold Studio Ltd. Powered by Pagecraft.</p>
</footer>

</body>
</html>
```